Calm and Clarity Health Flyer (new business startup)

One page...clear enough to be read if faxed. This mental health clinic treats depression/anxiety in kids and adults. It also treats opiate and alcohol addiction. It's in downtown Elmira, NY and the owner of the clinic is from Elmira NY, where it's located. This clinic does not take health insurance, so it charges a low rate of $75 a visit once they pay the $125 starting fee.

Target Market(s)

doctors offices, new patients

Industry/Entity Type

Doctor

Requirements
Must have
• see microsoft word document. pdf is printed on the company letterhead.
Nice to have
• a simplified map would be nice. if you can include the building it would be a plus. The same two fonts were used in the business cards and letter head (kennedy small caps boo*) and Refrigerator Delux.

```html
<!DOCTYPE html>
<html lang="en">
<head>
<meta charset="utf-8">
<title>Calm and Clarity Health</title>
<link rel="stylesheet" href="https://fonts.googleapis.com/css2?family=Cinzel:wght@400&family=Roboto+Condensed:wght@700&family=Roboto+Mono:wght@700&family=Roboto:wght@400;500;700&display=swap">
<style>
:root{
  --orange:#f26a3a;
  --blue:#2aa6dc;
  --ink:#2d2d2d;
  --white:#ffffff;
  --map-bg:#e9ecef;
  --photo-bg:#8a5a44;
}
*{margin:0;padding:0;box-sizing:border-box}
html,body{width:927px;height:1200px;overflow:hidden;background:var(--white)}
.flyer{position:relative;width:927px;height:1200px;font-family:'Roboto',sans-serif;color:var(--ink);background:var(--white)}
.brand{position:absolute;top:48px;left:0;width:927px;display:flex;justify-content:center;align-items:center;gap:18px}
.brand-dot{width:56px;height:56px;border-radius:50%;background:var(--orange)}
.brand-name{font-family:'Roboto Condensed',sans-serif;font-weight:700;font-size:40px;color:var(--orange);letter-spacing:-0.5px}
.provider-band{position:absolute;top:155px;left:0;width:927px;height:117px;background:var(--blue);color:var(--white);text-align:center}
.provider-name{font-family:'Cinzel',serif;font-size:47px;line-height:1;margin-top:14px;letter-spacing:0.5px}
.provider-title{font-family:'Roboto Mono',monospace;font-weight:700;font-size:23px;margin-top:12px;letter-spacing:2.5px}
.call{position:absolute;top:282px;left:0;width:927px;text-align:center;font-family:'Roboto Condensed',sans-serif;font-weight:700;font-size:64px;color:var(--orange);line-height:1}
.fees{position:absolute;top:358px;left:68px;width:792px;height:122px;background:var(--orange);border-radius:4px;color:var(--white);font-weight:700;font-size:32px;padding:15px 0 0 34px;line-height:1.26}
.fee{display:flex;width:722px;justify-content:space-between}
.hours{position:absolute;top:494px;left:0;width:927px;text-align:center;font-size:29px;font-family:'Roboto Condensed',sans-serif;font-weight:400}
.hours span{font-family:'Roboto',sans-serif;font-weight:400}
.ages{position:absolute;top:536px;left:0;width:927px;text-align:center;font-size:31px;font-weight:700}
.conditions-head{position:absolute;top:584px;left:92px;width:735px;display:flex;align-items:center;gap:6px}
.conditions-head::before,.conditions-head::after{content:"";flex:1;height:1.5px;background:var(--ink)}
.conditions-head h2{font-family:'Roboto Condensed',sans-serif;font-weight:700;font-size:35px;color:var(--orange)}
.conditions{position:absolute;top:630px;left:0;width:927px;text-align:center;font-size:32px;line-height:42px}
.sep{display:inline-block;width:12px;height:12px;border-radius:50%;background:var(--orange);margin:0 6px;vertical-align:middle}
.rule{position:absolute;top:722px;left:95px;width:732px;height:1.5px;background:var(--ink)}
.insurance{position:absolute;top:737px;left:30px;width:867px;text-align:center;font-size:20px;line-height:25px}
.insurance strong{font-weight:700}
.building{position:absolute;top:863px;left:49px;width:406px;height:205px;background:linear-gradient(180deg,#c9d9e6 0%,#9a6a52 35%,var(--photo-bg) 100%);border:1px solid #555}
.map{position:absolute;top:863px;left:470px;width:408px;height:205px;background:var(--map-bg);border:1px solid #555}
.substance{position:absolute;top:1074px;left:46px;width:832px;height:64px;background:var(--orange);color:var(--white);text-align:center;font-weight:700;font-size:19.5px;line-height:26px;padding-top:6px}
.footer{position:absolute;top:1147px;left:0;width:927px;height:53px;background:var(--blue);color:var(--white);display:flex;justify-content:center;align-items:center;gap:8px;font-size:21px}
.footer svg{width:18px;height:18px;fill:var(--white)}
</style>
</head>
<body>
<main class="flyer">
  <header class="brand">
    <div class="brand-dot"></div>
    <div class="brand-name">CALM AND CLARITY HEALTH</div>
  </header>

  <section class="provider-band">
    <h1 class="provider-name">DANIEL REYES, RPA, PLLC</h1>
    <p class="provider-title">Psychiatric Physician Assistant (PA-C, PSY-CAQ)</p>
  </section>

  <p class="call">CALL US :&nbsp; 607-555-0142</p>

  <section class="fees">
    <div class="fee"><span>Psychiatric Evaluation&nbsp; (45min) -</span><span>$125*</span></div>
    <div class="fee"><span>Psychiatric Office Visit (15min) -</span><span>$75*</span></div>
  </section>

  <p class="hours"><span>Hours:&nbsp; Monday &amp; Saturday 9 am - 4 pm</span></p>
  <p class="ages">AGES:&nbsp; 6 YEARS OLD AND UP</p>

  <div class="conditions-head"><h2>CONDITIONS TREATED</h2></div>
  <p class="conditions">
    Depression<span class="sep"></span>Anxiety<span class="sep"></span>PTSD<span class="sep"></span>ADHD<span class="sep"></span>Addiction<br>
    Bipolar<span class="sep"></span>Childhood Mood Disorders
  </p>
  <div class="rule"></div>

  <p class="insurance">*<strong>We work for you, not the insurance companies.</strong> Although we do not partner with any Health insurance, a bill will be provided to you for you to submit to your insurance company.</p>

  <div class="building" role="img" aria-label="Photo of the downtown brick office building housing the clinic"></div>
  <div class="map" role="img" aria-label="Street map of downtown Elmira showing the clinic location near the river"></div>

  <p class="substance">Calm and Clarity Health also treats substance use<br>disorders including opioids, Sedarin, and alcohol.</p>

  <footer class="footer">
    <span>250 N. Lake St #310, Elmira, NY 14901</span>
    <svg viewBox="0 0 24 24" aria-hidden="true"><path d="M6.6 10.8c1.4 2.8 3.8 5.1 6.6 6.6l2.2-2.2c.3-.3.7-.4 1-.2 1.1.4 2.3.6 3.6.6.6 0 1 .4 1 1V20c0 .6-.4 1-1 1C10.6 21 3 13.4 3 4c0-.6.4-1 1-1h3.5c.6 0 1 .4 1 1 0 1.3.2 2.5.6 3.6.1.3 0 .7-.2 1z"/></svg>
    <span>607-555-0142</span>
    <svg viewBox="0 0 24 24" aria-hidden="true"><path d="M6 3h10v5H6z M3 9h18v9h-3v3H6v-3H3z M8 15v4h8v-4z"/></svg>
    <span>607-555-0187</span>
  </footer>
</main>
</body>
</html>
```